【 概要 】 ホームページのTOP画像のデザインを募集いたします。 飲食店専用ホームページ制作です。 メインターゲットは飲食店オーナーの方々です。 飲食のホームページにあった「どんなお店なのか」、「どんなメニュ・どんなコースがあるか」など、 そのお店を気になった方々に来店を促すようなTOP画像が希望です。 【 依頼内容 】 ・サイズ:1920px×1080px ・作成数: 1種類 ・利用用途:ホームページトップ画像 ・色:オレンジ/赤/黄色 ・文言:あなたのお店をオリジナルデザインで作ってみませんか? 【 デザインイメージ 】 ・雰囲気:信頼感、安心感があり、ポップ感 ・現在制作途中のホームページにあった感じ http://sampwebnoren.com/ ・参考他社デザイン https://www.hanamuraya.co.jp/menu/kikaku/ また飲食以外も対象にしたいと思ったので別案も制作していただけたら幸いです。 【 依頼内容 】 色:グレー/白/黒 文言:ホームページはオリジナルデザインで! 参考URL:https://qv-webworks.jp/hp/?utm_source=kensaku&utm_medium=cpc&qclid=QRS.2004815367.PXbTwLcdFhZNruqk5p8w27AKRGetSd3hvm-qWFBCZjBXFgKQ5_E_CzX 【 契約金額(税抜) 】 1万円 ※契約金額(税込)からシステム利用料を差し引いた金額が、ワーカーさまの受取金額となります その他ご質問等ありましたら、気軽にお問い合わせください。 ご応募をお待ちしております! |
| https://www.hanamuraya.co.jp/menu/kikaku/ | ||
私共の内容をよく理解していただいた上で作成していただきありがとうございます。
今回korunote様のご提案が弊社のHPの表画面での使用に一番最適だと考え作用させていただきます。
皆様色々ご提案ありがとうございます。とても素敵なデザインを見していただきました。
弊社は今後よくご依頼などをさせていただきますので、その際は皆様また力を貸していただければと思います。

```html
<!DOCTYPE html>
<html lang="ja">
<head>
<meta charset="UTF-8">
<title>あなたのお店をオリジナルデザインで作ってみませんか？</title>
<link rel="stylesheet" href="https://fonts.googleapis.com/css2?family=M+PLUS+Rounded+1c:wght@800&display=swap">
<style>
  :root {
    --mustard-deep: #b98a1c;
    --mustard: #d9a72e;
    --mustard-light: #f3dc8a;
    --splash-yellow: #fbf25c;
    --headline-red: #e5231d;
    --outline-white: #ffffff;
    --shadow-brown: #7a4a10;
    --sketch-tone: rgba(120, 82, 18, 0.28);
  }
  html, body {
    margin: 0;
    padding: 0;
    overflow: hidden;
    background: #ffffff;
  }
  .hero {
    position: relative;
    width: 1200px;
    height: 676px;
    overflow: hidden;
    background: radial-gradient(ellipse 62% 70% at 50% 55%, var(--mustard-light) 0%, var(--mustard) 55%, var(--mustard-deep) 100%);
  }
  .hero__sketches,
  .hero__splash {
    position: absolute;
    inset: 0;
    width: 1200px;
    height: 676px;
  }
  .hero__headline {
    position: absolute;
    inset: 0;
    margin: 0;
    font-family: "M PLUS Rounded 1c", sans-serif;
    font-weight: 800;
    color: var(--headline-red);
  }
  .hero__line {
    position: absolute;
    display: block;
    white-space: nowrap;
    font-size: 60px;
    line-height: 1;
    letter-spacing: 0.02em;
    -webkit-text-stroke: 8px var(--outline-white);
    paint-order: stroke fill;
    text-shadow: 3px 4px 0 var(--shadow-brown);
  }
  .hero__line--first  { left: 338px; top: 190px; }
  .hero__line--second { left: 296px; top: 288px; }
  .hero__line--third  { left: 340px; top: 390px; }
</style>
</head>
<body>
  <main class="hero">
    <svg class="hero__sketches" viewBox="0 0 1200 676" role="img" aria-label="料理と食材の線画イラスト（トマト、ペッパーミル、まな板、フォーク、クロワッサン、玉ねぎ、ナイフ、ハーブ、パプリカ、グラスなど）が画面の周囲を囲む">
      <g fill="var(--sketch-tone)">
        <ellipse cx="150" cy="180" rx="70" ry="65"/>
        <ellipse cx="215" cy="70" rx="65" ry="55"/>
        <rect x="95" y="300" width="60" height="160" rx="25"/>
        <rect x="70" y="440" width="200" height="210" rx="20" transform="rotate(-35 170 545)"/>
        <rect x="350" y="10" width="140" height="26" rx="13" transform="rotate(-25 420 23)"/>
        <ellipse cx="590" cy="40" rx="80" ry="30"/>
        <ellipse cx="840" cy="120" rx="60" ry="70"/>
        <rect x="880" y="40" width="230" height="22" rx="11" transform="rotate(-30 995 51)"/>
        <ellipse cx="1120" cy="230" rx="50" ry="115"/>
        <ellipse cx="1060" cy="480" rx="90" ry="95"/>
        <rect x="860" y="560" width="300" height="22" rx="11" transform="rotate(25 1010 571)"/>
        <ellipse cx="490" cy="560" rx="100" ry="140" transform="rotate(-30 490 560)"/>
        <ellipse cx="280" cy="640" rx="70" ry="40"/>
        <rect x="600" y="540" width="170" height="90" rx="40" transform="rotate(15 685 585)"/>
        <ellipse cx="920" cy="330" rx="28" ry="28"/>
      </g>
    </svg>

    <svg class="hero__splash" viewBox="0 0 1200 676" aria-hidden="true">
      <path fill="var(--splash-yellow)" d="M300 150 C360 110 470 130 560 115 C660 100 760 95 860 120 C930 140 960 190 940 240 C985 270 1000 330 960 380 C990 420 1000 470 950 500 C880 540 790 520 720 545 C640 570 560 575 480 555 C400 540 330 560 280 520 C230 480 250 430 270 400 C230 360 230 300 270 270 C240 230 250 180 300 150 Z"/>
    </svg>

    <h1 class="hero__headline">
      <span class="hero__line hero__line--first">あなたのお店を</span>
      <span class="hero__line hero__line--second">オリジナルデザインで</span>
      <span class="hero__line hero__line--third">作ってみませんか？</span>
    </h1>
  </main>
</body>
</html>
```